Rack Card Design Project

We are a locally family owned public golf course. We would like to have a rack card designed that can be used for multiple applications. The colors in our logo are grey, blue, and white. Please use those in the card design. The company logo, contact information, address, and summer pricing should be included. I've included some pictures that may or may not be used. I'm also open to suggestions....use one photo, multiple photos, a stock photo or image representing golf etc.

```html
<!DOCTYPE html>
<html lang="en">
<head>
<meta charset="utf-8">
<title>Heron Bend Golf Club – Rack Card</title>
<link rel="stylesheet" href="https://fonts.googleapis.com/css2?family=Ubuntu:wght@500;700&family=Roboto+Condensed:ital,wght@0,500;1,700&family=Open+Sans:ital,wght@0,400;0,700;0,800;1,400&display=swap">
<style>
  :root{
    --page:#dcdde0;
    --sky:#0a9ad6;
    --ocean:#0a6fb5;
    --teal-deep:#0e4d6a;
    --navy:#12244a;
    --paper:#eeefea;
    --ink:#1c1c22;
    --grass:#3f9a2c;
    --grass-dark:#2c7a1e;
    --fairway:#5f8a48;
    --steel:#9a9c9e;
    --amber:#e0901e;
    --alert:#e0201a;
  }
  *{margin:0;padding:0;box-sizing:border-box}
  html,body{width:1200px;height:1200px;overflow:hidden;background:var(--page)}
  .sheet{position:relative;width:1200px;height:1200px}
  .rack-card{position:absolute;top:170px;width:470px;height:860px;overflow:hidden;box-shadow:0 6px 14px rgba(0,0,0,.18)}
  .rack-card--front{left:100px}
  .rack-card--back{left:630px}
  .rack-card svg.card-art{position:absolute;inset:0;width:470px;height:860px}
  .layer{position:absolute;left:0;width:100%;text-align:center}

  /* front */
  .brand{top:34px;left:36px;width:auto;display:flex;align-items:center;gap:12px;text-align:left}
  .brand-dot{width:58px;height:58px;border-radius:50%;background:var(--steel);flex:none}
  .brand-name{font-family:"Ubuntu",sans-serif;font-weight:700;font-size:22px;color:#fff;line-height:1.1}
  .front-contact{top:690px;color:var(--navy)}
  .front-contact .phone{font-family:"Roboto Condensed",sans-serif;font-size:29px;font-style:italic;font-weight:700}
  .front-contact .web{font-family:"Open Sans",sans-serif;font-weight:800;font-size:20px;margin-top:4px}
  .front-contact address{font-family:"Open Sans",sans-serif;font-style:italic;font-size:14px;line-height:1.25;margin-top:8px}

  /* back */
  .rates-tab{position:absolute;top:360px;left:0;width:250px;height:30px;background:#fff;clip-path:polygon(0 0,100% 0,92% 100%,0 100%)}
  .rates-tab span{display:block;padding-left:40px;font-family:"Ubuntu",sans-serif;font-weight:700;font-size:22px;line-height:30px;color:var(--ink)}
  .season{top:396px;font-family:"Open Sans",sans-serif;font-weight:700;font-size:30px;color:#fff}
  .rate-rule{position:absolute;height:1px;background:rgba(255,255,255,.75)}
  .rate{font-family:"Open Sans",sans-serif;font-weight:800;color:var(--ink)}
  .rate-head{top:446px;font-size:17px}
  .rate-times{top:474px;font-size:12px;color:#fff}
  .rate-times b{font-size:17px}
  .rate-late{top:502px;font-size:12px;color:#fff}
  .rate-late b{font-size:17px}
  .rate-nine{top:530px;font-size:18px}
  .rate-nine b,.rate-walk b{color:#fff;font-size:22px;margin-left:10px}
  .rate-walk{top:566px;font-size:18px}
  .lunch{top:620px;left:36px;width:220px;font-family:"Open Sans",sans-serif;font-weight:800;font-size:15px;line-height:1.2;color:#fff}
  .lunch span{color:var(--ink)}
  .kids-badge{position:absolute;left:284px;top:598px;width:138px;height:138px;border-radius:50%;background:var(--amber);border:4px solid #fff;display:flex;align-items:center;justify-content:center;text-align:center;font-family:"Open Sans",sans-serif;font-weight:800;font-size:14px;line-height:1.25;color:var(--ink)}
  .kids-badge em{font-style:normal;color:var(--alert);font-size:20px}
  .back-contact{top:742px;color:var(--ink)}
  .back-contact .phone{font-family:"Roboto Condensed",sans-serif;font-weight:500;font-size:26px}
  .back-contact .web{font-family:"Open Sans",sans-serif;font-size:22px;margin-top:2px}
</style>
</head>
<body>
<main class="sheet">

  <section class="rack-card rack-card--front">
    <svg class="card-art" viewBox="0 0 470 860">
      <defs>
        <linearGradient id="blueFront" x1="0" y1="0" x2="1" y2="0">
          <stop offset="0" stop-color="#0a9ad6"/><stop offset="1" stop-color="#0a6fb5"/>
        </linearGradient>
        <radialGradient id="turf" cx=".5" cy=".55" r=".7">
          <stop offset="0" stop-color="#4aa834"/><stop offset="1" stop-color="#2c7a1e"/>
        </radialGradient>
      </defs>
      <rect width="470" height="860" fill="var(--paper)"/>
      <rect width="470" height="180" fill="url(#blueFront)"/>
      <path d="M0,120 C60,70 150,62 230,92 S400,118 470,92 L470,180 L0,180Z" fill="var(--teal-deep)"/>
      <path role="img" aria-label="Photo of a golf club and ball resting on green turf" d="M0,145 C70,98 160,92 240,118 S400,128 470,104 L470,640 C400,680 300,640 200,615 C120,598 50,610 0,640Z" fill="url(#turf)"/>
      <path d="M0,640 C50,605 120,590 200,600 C300,615 380,665 470,640 L470,700 L0,700Z" fill="var(--teal-deep)"/>
      <path d="M0,660 C50,630 130,618 220,628 C320,640 400,670 470,648 L470,700 L0,700Z" fill="var(--ocean)"/>
      <path d="M0,672 C60,645 150,636 240,646 C330,656 410,672 470,654 L470,860 L0,860Z" fill="var(--paper)"/>
    </svg>
    <div class="layer brand">
      <span class="brand-dot"></span>
      <span class="brand-name">Heron Bend<br>Golf Club</span>
    </div>
    <div class="layer front-contact">
      <p class="phone">call us: 555-014-2208</p>
      <p class="web">www.heronbendgc.com</p>
      <address>Heron Bend Golf Club<br>410 Cypress Hollow Rd<br>Palm Harbor, FL 34000</address>
    </div>
  </section>

  <section class="rack-card rack-card--back">
    <svg class="card-art" viewBox="0 0 470 860">
      <defs>
        <linearGradient id="blueBack" x1="0" y1="0" x2="1" y2="1">
          <stop offset="0" stop-color="#0a9ad6"/><stop offset="1" stop-color="#0a6fb5"/>
        </linearGradient>
      </defs>
      <rect width="470" height="860" fill="url(#blueBack)"/>
      <path d="M0,85 C70,50 160,55 240,85 S400,105 470,85 L470,140 L0,140Z" fill="var(--teal-deep)"/>
      <path role="img" aria-label="Photo of the golf course fairway lined with palm trees" d="M0,100 C70,68 160,72 240,98 S400,118 470,98 L470,315 C400,290 300,295 220,310 C140,325 60,330 0,305Z" fill="var(--fairway)"/>
      <path d="M0,305 C60,330 140,325 220,310 C300,295 400,290 470,315 L470,330 C400,312 300,315 220,332 C140,350 60,350 0,330Z" fill="var(--teal-deep)"/>
      <path d="M0,700 C60,660 150,650 240,670 C330,690 400,700 470,690 L470,740 L0,740Z" fill="var(--teal-deep)"/>
      <path d="M0,730 C60,700 160,690 250,705 C340,720 420,725 470,700 L470,860 L0,860Z" fill="var(--paper)"/>
    </svg>
    <div class="rates-tab"><span>Summer Rates</span></div>
    <p class="layer season">May 1 – September 30</p>
    <span class="rate-rule" style="top:441px;left:90px;width:290px"></span>
    <p class="layer rate rate-head">18 Holes With Cart</p>
    <p class="layer rate rate-times">7AM – 11AM <b>$24</b> &nbsp;|&nbsp; 11AM – 3PM <b>$19</b></p>
    <p class="layer rate rate-late">3PM – Close <b>$15</b></p>
    <span class="rate-rule" style="top:525px;left:95px;width:290px"></span>
    <p class="layer rate rate-nine">9 Holes With Cart <b>$15</b></p>
    <span class="rate-rule" style="top:559px;left:100px;width:290px"></span>
    <p class="layer rate rate-walk">Walking <b>$12</b></p>
    <p class="layer lunch">Lunch Available Daily<br><span>10AM – 3PM</span></p>
    <div class="kids-badge"><p>Children 15<br>and Under<br><em>free</em> with<br>Paid Adult</p></div>
    <div class="layer back-contact">
      <p class="phone">call us: 555-014-2208</p>
      <p class="web">www.heronbendgc.com</p>
    </div>
  </section>

</main>
</body>
</html>
```